Brightpath Wellness Partners

Please design a business card that is colorful but at the same time easy to read. We are based out on Miami Florida. We are a small start up healthcare company that has been in operation for 1 year. Our clients are Hospitals, Insurance companies, and Manage Care health companies. We are growing quickly and lead the niche we are in. Please make the card 2 sided on the front will be the typical info. Logo, Company Name, Persons Name, Title, Cell #, Office #, Fax#, email, website. No address. On the back we will list 5 services that we do. For example Care Transitions, Case management, Risk assessment, Utilization Review.
Target Market(s)
CEO's and COO's of hospitals and healthcare companies.
Industry/Entity Type
Healthcare

```html
<!DOCTYPE html>
<html lang="en">
<head>
<meta charset="utf-8">
<title>Brightpath Wellness Partners – Business Card</title>
<link href="https://fonts.googleapis.com/css2?family=Source+Sans+3:wght@300;400;600;700&display=swap" rel="stylesheet">
<style>
  :root {
    --backdrop: #e6e3df;
    --card: #f3f3f3;
    --ink: #4a4a4a;
    --ink-soft: #5e5e5e;
    --navy: #2b2f8f;
    --blue: #1f3f9e;
    --green: #3a9a36;
    --yellow: #e2c514;
    --red: #d8262c;
    --strip: #505256;
  }
  * { box-sizing: border-box; margin: 0; padding: 0; }
  html, body { width: 1200px; height: 900px; overflow: hidden; }
  body {
    background: var(--backdrop);
    font-family: "Source Sans 3", Arial, sans-serif;
    color: var(--ink);
    position: relative;
  }
  .card {
    position: absolute;
    left: 320px;
    width: 560px;
    height: 320px;
    background: var(--card);
    box-shadow: 0 6px 18px rgba(0,0,0,0.12);
    overflow: hidden;
  }
  .card--back { top: 90px; }
  .card--front { top: 470px; }

  /* back side */
  .edge-strip {
    position: absolute; top: 0; right: 0;
    width: 24px; height: 100%;
    background: var(--strip);
  }
  .edge-strip span { display: block; height: 22px; }
  .edge-strip span:nth-child(1) { margin-top: 70px; background: var(--blue); }
  .edge-strip span:nth-child(2) { background: var(--green); }
  .edge-strip span:nth-child(3) { background: var(--yellow); }
  .edge-strip span:nth-child(4) { background: var(--red); }

  .brand-mark {
    position: absolute; left: 50px; top: 120px;
    display: flex; align-items: center; gap: 14px;
  }
  .brand-mark .dot {
    width: 26px; height: 26px; border-radius: 50%;
    background: var(--navy);
  }
  .brand-mark .name {
    font-weight: 700; font-size: 26px; line-height: 1.05;
    color: var(--navy);
  }
  .services {
    position: absolute; left: 330px; top: 42px;
    list-style: none;
    font-size: 17px; line-height: 1.55; color: var(--ink);
  }
  .services li::before { content: "• "; }

  /* front side */
  .front-brand {
    position: absolute; left: 40px; top: 58px;
    display: flex; align-items: center; gap: 12px;
  }
  .front-brand .dot {
    width: 22px; height: 22px; border-radius: 50%;
    background: var(--navy);
  }
  .front-brand .name {
    font-weight: 700; font-size: 24px; line-height: 1.05;
    color: var(--navy);
  }
  .person {
    position: absolute; left: 40px; top: 190px;
  }
  .person__name {
    font-weight: 300; font-size: 30px; letter-spacing: 0.5px;
    color: var(--ink); text-transform: uppercase;
  }
  .person__title {
    font-size: 17px; color: var(--ink-soft); margin-top: 2px;
  }
  .contact {
    position: absolute; left: 320px; top: 60px;
    list-style: none;
    font-size: 15px; line-height: 1.5; color: var(--ink);
  }
  .contact b {
    display: inline-block; width: 18px; font-weight: 700;
  }
  .contact .t b { color: var(--blue); }
  .contact .m b { color: var(--green); }
  .contact .f b { color: var(--yellow); }
  .contact .e b { color: var(--red); }
  .website {
    position: absolute; left: 320px; top: 190px;
    font-weight: 700; font-size: 16px; color: var(--ink);
  }
</style>
</head>
<body>

  <section class="card card--back" aria-label="Card back">
    <div class="brand-mark">
      <span class="dot"></span>
      <span class="name">Brightpath<br>Wellness Partners</span>
    </div>
    <ul class="services">
      <li>Care Transitions</li>
      <li>Case management</li>
      <li>Risk assessment</li>
      <li>Utilization Review</li>
    </ul>
    <div class="edge-strip"><span></span><span></span><span></span><span></span></div>
  </section>

  <section class="card card--front" aria-label="Card front">
    <div class="front-brand">
      <span class="dot"></span>
      <span class="name">Brightpath<br>Wellness<br>Partners</span>
    </div>
    <div class="person">
      <p class="person__name">Daniel Morrow</p>
      <p class="person__title">Operation Manager</p>
    </div>
    <ul class="contact">
      <li class="t"><b>T</b>(305) 555 0142</li>
      <li class="m"><b>M</b>(305) 555 0187</li>
      <li class="f"><b>F</b>(305) 555 0143</li>
      <li class="e"><b>E</b>daniel@brightpathwellness.com</li>
    </ul>
    <p class="website">www.brightpathwellness.com</p>
  </section>

</body>
</html>
```